Logo & Visitenkarte für Arzt und Psychotherapeut
Zielgruppe
Facharzt für Kinder- und Jugendpsychiatrie und Psychotherapie
Tätigkeiten in der Ausbildung, Hochschuldozent, Supervisor
Gesundheitsökonom
Aufgabenstellung
Im Logo Aufnahme eines Kind/Familienorientierten Designs
Vielleicht angelehnt an Logo des Birkenau Klangsommer-Festivals
Lieblingsfarbe blau

```html
<!DOCTYPE html>
<html lang="de">
<head>
<meta charset="utf-8">
<title>Jonas Wendelberg – Visitenkarten</title>
<link href="https://fonts.googleapis.com/css2?family=Roboto:wght@300;400;500&family=Montserrat:wght@400&family=Open+Sans:wght@400&display=swap" rel="stylesheet">
<style>
  :root {
    --page: #ffffff;
    --board: #404042;
    --card: #f0f0f1;
    --card-white: #ffffff;
    --navy: #003f58;
    --teal: #0aa3c4;
    --grey-text: #8a8b8d;
    --dark-text: #4a4a4c;
    --mark: #7fb8c9;
    --label: #ffffff;
  }
  * { margin: 0; padding: 0; box-sizing: border-box; }
  html, body { width: 1200px; height: 1200px; overflow: hidden; background: var(--page); }
  .board { position: absolute; left: 69px; top: 0; width: 1061px; height: 1200px; background: var(--board); }
  .card { position: absolute; background: var(--card); box-shadow: 6px 8px 10px rgba(0,0,0,.45); overflow: hidden; font-family: "Roboto", Arial, sans-serif; }
  .card.white { background: var(--card-white); }
  .card.navy { background: var(--navy); }
  .variant-label { position: absolute; font-family: "Open Sans", Arial, sans-serif; color: var(--label); font-size: 30px; line-height: 1; }
  .mark { position: absolute; border-radius: 50%; background: var(--mark); }
  .abs { position: absolute; white-space: nowrap; line-height: 1; }
  .title { color: var(--grey-text); font-weight: 300; }
  .first { color: var(--grey-text); font-weight: 300; }
  .surname { color: var(--teal); font-weight: 500; }
  .role-teal { color: var(--teal); font-weight: 400; }
  .tagline { font-family: "Montserrat", Arial, sans-serif; color: var(--dark-text); }
  .navy .title, .navy .first, .navy .tagline { color: #ffffff; }
  .contact { font-size: 8.4px; color: var(--dark-text); line-height: 10.5px; }
  .contact svg { width: 7px; height: 7px; vertical-align: -1px; margin-right: 3px; fill: var(--teal); }
  .person { color: var(--dark-text); font-weight: 300; }
  .role { color: var(--dark-text); font-weight: 300; }
  .divider { position: absolute; width: 1px; background: var(--grey-text); }
</style>
</head>
<body>
<div class="board">

  <!-- Logo presentation, horizontal -->
  <div class="card" style="left:88px;top:68px;width:403px;height:236px;">
    <div class="mark" style="left:34px;top:64px;width:118px;height:118px;"></div>
    <div class="abs title" style="left:161px;top:89px;font-size:21px;">Dr. med.</div>
    <div class="abs first" style="left:160px;top:108px;font-size:31px;">Jonas</div>
    <div class="abs surname" style="left:160px;top:134px;font-size:31px;">Wendelberg</div>
    <div class="abs tagline" style="left:161px;top:168px;font-size:7.6px;">Kinder- und Jugendpsychiatrie und Psychotherapie</div>
  </div>

  <!-- Logo presentation, stacked -->
  <div class="card" style="left:528px;top:65px;width:403px;height:236px;">
    <div class="mark" style="left:134px;top:27px;width:130px;height:130px;"></div>
    <div class="abs title" style="left:69px;top:142px;font-size:16px;">Dr. med.</div>
    <div class="abs" style="left:0;width:403px;text-align:center;top:157px;font-size:34px;"><span class="first">Jonas</span><span class="surname">Wendelberg</span></div>
    <div class="abs tagline" style="left:0;width:403px;text-align:center;top:197px;font-size:10.5px;">Kinder- und Jugendpsychiatrie und Psychotherapie</div>
  </div>

  <div class="variant-label" style="left:94px;top:368px;">1</div>
  <div class="card" style="left:141px;top:371px;width:315px;height:204px;">
    <div class="mark" style="left:105px;top:30px;width:98px;height:98px;"></div>
    <div class="abs title" style="left:59px;top:116px;font-size:12px;">Dr. med.</div>
    <div class="abs" style="left:0;width:315px;text-align:center;top:129px;font-size:25px;"><span class="first">Jonas</span><span class="surname">Wendelberg</span></div>
    <div class="abs tagline" style="left:0;width:315px;text-align:center;top:157px;font-size:8px;">Kinder- und Jugendpsychiatrie und Psychotherapie</div>
  </div>

  <div class="variant-label" style="left:572px;top:368px;">A</div>
  <div class="card" style="left:620px;top:371px;width:315px;height:204px;">
    <div class="mark" style="left:213px;top:8px;width:80px;height:80px;"></div>
    <div class="abs person" style="left:20px;top:88px;font-size:20px;">Jonas Wendelberg</div>
    <div class="abs role" style="left:22px;top:108px;font-size:8.5px;">Psychotherapeut</div>
    <div class="abs contact" style="left:18px;top:135px;">
      <svg viewBox="0 0 10 10"><path d="M5 0a3.5 3.5 0 0 1 3.5 3.5C8.5 6 5 10 5 10S1.5 6 1.5 3.5A3.5 3.5 0 0 1 5 0zm0 2a1.5 1.5 0 1 0 0 3 1.5 1.5 0 0 0 0-3z"/></svg>xxxxxxxxxxxxxxxxstraße 42<br>&nbsp;&nbsp;&nbsp;DE-0000000 XXXXXXXX
    </div>
    <div class="abs contact" style="left:160px;top:135px;">
      <svg viewBox="0 0 10 10"><rect x="2.5" y="0" width="5" height="10" rx="1"/></svg>+49-00-0000000000000<br>
      <svg viewBox="0 0 10 10"><path d="M0 4c2-3 8-3 10 0v1H7V4H3v1H0zM2 6h6l1 4H1z"/></svg>+49-00-0000000000000<br>
      <svg viewBox="0 0 10 10"><path d="M0 3c2-3 8-3 10 0v1H0zM2 5h6v5H2z"/></svg>+49-00-0000000000000<br>
      <div style="height:5px"></div>
      <svg viewBox="0 0 10 10"><path d="M0 2h10v6H0zM0 2l5 4 5-4" fill="none" stroke="#0aa3c4" stroke-width="1.2"/></svg>info@jonas-wendelberg.de<br>
      <svg viewBox="0 0 10 10"><circle cx="5" cy="5" r="4.3" fill="none" stroke="#0aa3c4"/><path d="M1 5h8M5 1v8" stroke="#0aa3c4" fill="none"/></svg>www.jonas-wendelberg.de
    </div>
  </div>

  <div class="variant-label" style="left:94px;top:631px;">2</div>
  <div class="card navy" style="left:141px;top:643px;width:315px;height:203px;">
    <div class="mark" style="left:105px;top:30px;width:98px;height:98px;"></div>
    <div class="abs title" style="left:59px;top:116px;font-size:12px;">Dr. med.</div>
    <div class="abs" style="left:0;width:315px;text-align:center;top:129px;font-size:25px;"><span class="first">Jonas</span><span class="surname">Wendelberg</span></div>
    <div class="abs tagline" style="left:0;width:315px;text-align:center;top:157px;font-size:8px;">Kinder- und Jugendpsychiatrie und Psychotherapie</div>
  </div>

  <div class="variant-label" style="left:572px;top:640px;">B</div>
  <div class="card" style="left:620px;top:643px;width:315px;height:204px;">
    <div class="mark" style="left:28px;top:20px;width:98px;height:98px;"></div>
    <div class="abs title" style="left:132px;top:39px;font-size:17px;">Dr. med.</div>
    <div class="abs first" style="left:131px;top:56px;font-size:24px;">Jonas</div>
    <div class="abs surname" style="left:131px;top:77px;font-size:24px;">Wendelberg</div>
    <div class="abs tagline" style="left:132px;top:104px;font-size:6.2px;">Kinder- und Jugendpsychiatrie und Psychotherapie</div>
    <div class="abs contact" style="left:18px;top:135px;">
      <svg viewBox="0 0 10 10"><path d="M5 0a3.5 3.5 0 0 1 3.5 3.5C8.5 6 5 10 5 10S1.5 6 1.5 3.5A3.5 3.5 0 0 1 5 0zm0 2a1.5 1.5 0 1 0 0 3 1.5 1.5 0 0 0 0-3z"/></svg>xxxxxxxxxxxxxxxxstraße 42<br>&nbsp;&nbsp;&nbsp;DE-0000000 XXXXXXXX
    </div>
    <div class="abs contact" style="left:160px;top:135px;">
      <svg viewBox="0 0 10 10"><rect x="2.5" y="0" width="5" height="10" rx="1"/></svg>+49-00-0000000000000<br>
      <svg viewBox="0 0 10 10"><path d="M0 4c2-3 8-3 10 0v1H7V4H3v1H0zM2 6h6l1 4H1z"/></svg>+49-00-0000000000000<br>
      <svg viewBox="0 0 10 10"><path d="M0 3c2-3 8-3 10 0v1H0zM2 5h6v5H2z"/></svg>+49-00-0000000000000<br>
      <div style="height:5px"></div>
      <svg viewBox="0 0 10 10"><path d="M0 2h10v6H0zM0 2l5 4 5-4" fill="none" stroke="#0aa3c4" stroke-width="1.2"/></svg>info@jonas-wendelberg.de<br>
      <svg viewBox="0 0 10 10"><circle cx="5" cy="5" r="4.3" fill="none" stroke="#0aa3c4"/><path d="M1 5h8M5 1v8" stroke="#0aa3c4" fill="none"/></svg>www.jonas-wendelberg.de
    </div>
  </div>

  <div class="variant-label" style="left:94px;top:905px;">3</div>
  <div class="card" style="left:141px;top:907px;width:315px;height:204px;">
    <div class="mark" style="left:84px;top:37px;width:134px;height:134px;"></div>
    <div class="abs contact" style="left:0;width:315px;text-align:center;top:184px;font-size:8.5px;">www.jonas-wendelberg.de</div>
  </div>

  <div class="variant-label" style="left:572px;top:909px;">C</div>
  <div class="card white" style="left:618px;top:907px;width:318px;height:205px;">
    <div class="mark" style="left:51px;top:16px;width:94px;height:94px;"></div>
    <div class="abs person" style="right:176px;top:120px;font-size:19px;line-height:1.05;text-align:right;">Jonas<br>Wendelberg</div>
    <div class="abs role-teal" style="right:176px;top:166px;font-size:8.5px;">Psychotherapeut</div>
    <div class="divider" style="left:154px;top:104px;height:80px;"></div>
    <div class="abs contact" style="left:169px;top:106px;font-size:8px;line-height:10px;">
      XXXXXXXXstrasse 1<br>0000000 XXXXXXXXXXX<br><div style="height:10px"></div>
      T.+49-00-0000000000000<br>F.+49-00-0000000000000<br><div style="height:10px"></div>
      info@jonas-wendelberg.de<br>www.jonas-wendelberg.de
    </div>
  </div>

</div>
</body>
</html>
```